Marbleton Health group for a medical office

We need a website created that for our new medical office that will support online booking for appointments. You designed the logo already.

```html
<!DOCTYPE html>
<html lang="en">
<head>
<meta charset="utf-8">
<title>Marbleton Health</title>
<link rel="stylesheet" href="https://fonts.googleapis.com/css2?family=Inter:wght@400;500;600;700&family=Playfair+Display:wght@700;800&display=swap">
<style>
:root{
  --primary:#2b8cc4;
  --teal:#2f9a95;
  --ink:#1b2433;
  --text:#5b6675;
  --muted:#7a8594;
  --soft:#eef3f5;
  --card:#f7f9fa;
  --line:#e3e8ec;
  --tag-bg:#e2f0f4;
  --tag-ink:#2b7fa8;
  --footer:#222a3a;
  --footer-text:#c5cbd5;
  --white:#ffffff;
}
*{box-sizing:border-box;margin:0;padding:0}
html,body{width:1200px;height:3909px;overflow:hidden}
body{font-family:"Inter",sans-serif;color:var(--ink);background:var(--white);position:relative}
.serif{font-family:"Playfair Display",serif}
a{color:inherit;text-decoration:none}
ul{list-style:none}

/* nav */
.site-nav{position:absolute;top:0;left:0;width:1200px;height:67px;background:#f6f7f8;border-bottom:1px solid var(--line);display:flex;align-items:center;padding:0 120px}
.brand{display:flex;align-items:center;gap:10px;font-weight:700;font-size:20px;color:var(--ink)}
.brand-dot{width:32px;height:32px;border-radius:50%;background:var(--primary)}
.nav-links{display:flex;gap:32px;margin-left:auto;margin-right:48px;font-size:14px;color:var(--ink)}
.btn{display:inline-flex;align-items:center;justify-content:center;gap:8px;font-weight:600;font-size:14px;border-radius:8px}
.btn-primary{background:var(--primary);color:var(--white)}
.nav-cta{width:152px;height:36px;border-radius:20px;font-size:13px}

/* hero */
.hero{position:absolute;top:67px;left:0;width:1200px;height:585px;overflow:hidden}
.hero-photo{position:absolute;inset:0;background:linear-gradient(100deg,#5a7590 0%,#7d97ad 40%,#b9cbd6 70%,#d6e0e6 100%)}
.hero-body{position:absolute;left:144px;top:190px;width:560px;color:var(--white)}
.hero h1{font-size:47px;line-height:1.1;font-weight:800;letter-spacing:-.5px}
.hero p{margin-top:18px;font-size:15px;line-height:1.45;opacity:.95}
.hero-actions{display:flex;gap:12px;margin-top:28px}
.hero-actions .btn{height:41px}
.btn-outline{border:2px solid var(--white);color:var(--white);width:136px}

/* about */
.about{position:absolute;top:652px;left:0;width:1200px;height:726px;background:var(--soft)}
.about-photo{position:absolute;left:120px;top:72px;width:456px;height:582px;border-radius:12px;background:linear-gradient(180deg,#d4dde4 0%,#c9b39a 45%,#e9ecef 75%,#2d4a74 100%)}
.stat-badge{position:absolute;left:372px;top:598px;width:180px;height:75px;background:var(--white);border-radius:10px;box-shadow:0 8px 24px rgba(20,40,60,.12);display:flex;align-items:center;gap:12px;padding:0 18px;white-space:nowrap}
.icon-circle{width:32px;height:32px;border-radius:50%;background:var(--tag-bg);display:flex;align-items:center;justify-content:center;flex:none}
.stat-badge strong{display:block;font-family:"Playfair Display",serif;font-size:16px}
.stat-badge span{font-size:10.5px;color:var(--muted)}
.about-copy{position:absolute;left:623px;top:136px;width:458px}
.tag{display:inline-block;background:var(--tag-bg);color:var(--tag-ink);font-size:11px;padding:5px 12px;border-radius:12px}
.about-copy h2{margin-top:14px;font-size:36px;line-height:1.03;font-weight:800;letter-spacing:-1px}
.about-copy .lead{margin-top:22px;font-size:13.5px;line-height:1.62;color:var(--text)}
.about-copy .sub{margin-top:18px;font-size:12.5px;line-height:1.6;color:var(--muted)}
.features{display:grid;grid-template-columns:1fr 1fr;gap:22px 16px;margin-top:24px}
.feature{display:flex;gap:12px}
.feature .icon-sq{width:30px;height:30px;border-radius:8px;background:#dcebf2;display:flex;align-items:center;justify-content:center;flex:none}
.feature h4{font-family:"Playfair Display",serif;font-size:13px;margin-bottom:4px}
.feature p{font-size:10.5px;line-height:1.45;color:var(--muted)}

/* section heads */
.section-head{text-align:center;width:600px;margin:0 auto}
.section-head h2{margin-top:12px;font-size:38px;line-height:1.05;font-weight:800;letter-spacing:-.5px}
.section-head p{margin-top:20px;font-size:14px;line-height:1.55;color:var(--text)}

/* services */
.services{position:absolute;top:1378px;left:0;width:1200px;height:659px;background:var(--white);padding-top:37px}
.service-cards{position:absolute;top:268px;left:120px;display:flex;gap:24px}
.service-card{width:304px;height:332px;background:var(--card);border:1px solid var(--line);border-radius:12px;padding:24px}
.service-icon{width:42px;height:38px;border-radius:8px;background:var(--teal);display:flex;align-items:center;justify-content:center}
.service-card h3{margin-top:24px;font-family:"Playfair Display",serif;font-size:16px}
.service-card p{margin-top:14px;font-size:12.5px;line-height:1.55;color:var(--text)}
.service-card ul{margin-top:14px;font-size:11px;color:var(--ink);line-height:1.9}
.service-card li::before{content:"";display:inline-block;width:5px;height:5px;border-radius:50%;background:var(--teal);margin-right:8px;vertical-align:middle}
.more{display:inline-flex;align-items:center;gap:8px;margin-top:14px;font-size:11px;color:var(--primary);font-weight:500}

/* portfolio */
.portfolio{position:absolute;top:2037px;left:0;width:1200px;height:743px;background:var(--soft);padding-top:21px}
.gallery{position:absolute;top:198px;left:120px;display:grid;grid-template-columns:repeat(3,308px);gap:17px 18px}
.gallery-item{height:230px;border-radius:4px}

/* contact */
.contact{position:absolute;top:2780px;left:0;width:1200px;height:765px;background:var(--white);padding-top:43px}
.contact-info{position:absolute;left:120px;top:230px;width:456px}
.contact-info h3{font-family:"Playfair Display",serif;font-size:18px;margin-bottom:22px}
.info-grid{display:grid;grid-template-columns:219px 219px;gap:20px 18px}
.info-card{height:136px;background:#eef1f3;border-radius:10px;padding:18px}
.info-card .service-icon{width:36px;height:34px}
.info-card h4{margin-top:16px;font-family:"Playfair Display",serif;font-size:12px}
.info-card p{margin-top:6px;font-size:10.5px;line-height:1.45;color:var(--text)}
.contact-form{position:absolute;left:623px;top:220px;width:457px;height:487px;background:var(--card);border:1px solid var(--line);border-radius:12px;padding:26px 24px}
.contact-form h3{font-family:"Playfair Display",serif;font-size:18px}
.field-row{display:grid;grid-template-columns:1fr 1fr;gap:14px}
.field{margin-top:14px}
.field label{display:block;font-size:10.5px;font-weight:500;margin-bottom:6px}
.input{height:36px;border:1px solid #d8dee4;border-radius:6px;background:var(--white);padding:0 12px;display:flex;align-items:center;font-size:12px;color:var(--muted)}
.textarea{height:92px;align-items:flex-start;padding-top:12px}
.consent{display:flex;gap:8px;margin-top:16px;font-size:10px;line-height:1.4;color:var(--muted)}
.consent i{width:10px;height:10px;border:1px solid #aab3bd;border-radius:2px;flex:none;margin-top:2px}
.send{width:100%;height:36px;margin-top:14px;font-size:12px}
.fine{margin-top:14px;text-align:center;font-size:8.5px;line-height:1.4;color:var(--muted)}

/* footer */
.site-footer{position:absolute;top:3545px;left:0;width:1200px;height:364px;background:var(--footer);color:var(--footer-text)}
.footer-cols{position:absolute;left:144px;top:76px;display:grid;grid-template-columns:237px 237px 237px 240px}
.footer-brand{font-family:"Playfair Display",serif;font-size:18px;color:var(--white);font-weight:700}
.footer-cols h5{font-family:"Playfair Display",serif;font-size:13px;color:var(--white);margin-top:-4px}
.footer-about{margin-top:22px;font-size:11px;line-height:1.55;width:180px}
.socials{display:flex;gap:12px;margin-top:18px}
.socials span{width:30px;height:30px;border-radius:50%;background:#343d4f}
.footer-list{margin-top:22px;font-size:11px;line-height:2.45}
.footer-contact{margin-top:22px;font-size:11px;line-height:1.8}
.footer-contact p+p{margin-top:10px}
.footer-bottom{position:absolute;left:144px;right:144px;top:295px;border-top:1px solid #39425a;padding-top:20px;display:flex;font-size:11px}
.footer-bottom nav{margin-left:auto;display:flex;gap:18px}
</style>
</head>
<body>

<header class="site-nav">
  <a class="brand" href="#"><span class="brand-dot"></span>Marbleton Health</a>
  <nav class="nav-links"><a href="#">Home</a><a href="#">About</a><a href="#">Services</a><a href="#">Portfolio</a><a href="#">Contact</a></nav>
  <a class="btn btn-primary nav-cta" href="#">Book Appointment</a>
</header>

<section class="hero">
  <div class="hero-photo" role="img" aria-label="Two doctors in white coats consulting with a patient in a bright clinic room"></div>
  <div class="hero-body">
    <h1 class="serif">Your Health, Our Priority</h1>
    <p>Experience compassionate care with our team of dedicated medical professionals. We're here to guide you on your journey to better health.</p>
    <div class="hero-actions">
      <a class="btn btn-primary" style="width:198px" href="#">
        <svg width="13" height="13" viewBox="0 0 24 24" fill="none" stroke="#fff" stroke-width="2"><rect x="3" y="5" width="18" height="16" rx="2"/><path d="M3 10h18M8 3v4M16 3v4"/></svg>
        Book Appointment</a>
      <a class="btn btn-outline" href="#">Learn More</a>
    </div>
  </div>
</section>

<section class="about">
  <div class="about-photo" role="img" aria-label="Portrait of a smiling doctor with a stethoscope"></div>
  <div class="stat-badge">
    <span class="icon-circle"><svg width="16" height="16" viewBox="0 0 24 24" fill="none" stroke="#2f9a95" stroke-width="2"><circle cx="12" cy="9" r="6"/><path d="M8.5 14l-1.5 8 5-3 5 3-1.5-8"/></svg></span>
    <div><strong>25+</strong><span>Years of Excellence</span></div>
  </div>
  <div class="about-copy">
    <span class="tag">About Marbleton Health</span>
    <h2 class="serif">Caring for You, Every Step of the Way</h2>
    <p class="lead">At Marbleton Health, we believe healthcare should be accessible, compassionate, and personalized. Our modern medical practice combines cutting-edge technology with genuine human connection to deliver exceptional care that puts your needs first.</p>
    <p class="sub">Founded with a vision to transform the patient experience, we've built a practice where every interaction matters. From routine check-ups to specialized treatments, our dedicated team ensures you receive the attention and expertise you deserve.</p>
    <div class="features">
      <div class="feature"><span class="icon-sq"><svg width="14" height="14" viewBox="0 0 24 24" fill="none" stroke="#2b8cc4" stroke-width="2"><path d="M12 21s-8-5-8-11a4.5 4.5 0 0 1 8-2.8A4.5 4.5 0 0 1 20 10c0 6-8 11-8 11z"/></svg></span><div><h4>Patient-Centered Care</h4><p>Your health and comfort are at the heart of everything we do.</p></div></div>
      <div class="feature"><span class="icon-sq"><svg width="14" height="14" viewBox="0 0 24 24" fill="none" stroke="#2b8cc4" stroke-width="2"><path d="M12 3l8 3v6c0 5-4 8-8 9-4-1-8-4-8-9V6z"/></svg></span><div><h4>Trusted Expertise</h4><p>Board-certified physicians with decades of combined experience.</p></div></div>
      <div class="feature"><span class="icon-sq"><svg width="14" height="14" viewBox="0 0 24 24" fill="none" stroke="#2b8cc4" stroke-width="2"><circle cx="9" cy="8" r="3.5"/><path d="M2 20c0-4 3-6 7-6s7 2 7 6M16 4.5a3.5 3.5 0 0 1 0 7M18 14c2.5.6 4 2.5 4 6"/></svg></span><div><h4>Personalized Approach</h4><p>Customized treatment plans tailored to your unique needs.</p></div></div>
      <div class="feature"><span class="icon-sq"><svg width="14" height="14" viewBox="0 0 24 24" fill="none" stroke="#2b8cc4" stroke-width="2"><circle cx="12" cy="9" r="6"/><path d="M8.5 14l-1.5 8 5-3 5 3-1.5-8"/></svg></span><div><h4>Excellence in Care</h4><p>Recognized for outstanding patient outcomes and satisfaction.</p></div></div>
    </div>
  </div>
</section>

<section class="services">
  <div class="section-head">
    <span class="tag">Our Services</span>
    <h2 class="serif">Comprehensive Healthcare Solutions</h2>
    <p>We offer a full range of medical services designed to meet your health needs at every stage of life, all under one roof.</p>
  </div>
  <div class="service-cards">
    <article class="service-card">
      <span class="service-icon"><svg width="20" height="20" viewBox="0 0 24 24" fill="none" stroke="#fff" stroke-width="2"><path d="M5 3v6a5 5 0 0 0 10 0V3M10 14v2a5 5 0 0 0 10 0v-2"/><circle cx="20" cy="12" r="2"/></svg></span>
      <h3>Primary Care</h3>
      <p>Comprehensive health services including annual physicals, preventive care, chronic disease management, and same-day appointments for urgent needs.</p>
      <ul><li>Annual Wellness Exams</li><li>Chronic Disease Management</li><li>Vaccinations &amp; Immunizations</li></ul>
      <a class="more" href="#">Learn More <svg width="10" height="10" viewBox="0 0 24 24" fill="none" stroke="#2b8cc4" stroke-width="2.5"><path d="M4 12h16M14 6l6 6-6 6"/></svg></a>
    </article>
    <article class="service-card">
      <span class="service-icon"><svg width="20" height="20" viewBox="0 0 24 24" fill="none" stroke="#fff" stroke-width="2"><circle cx="12" cy="12" r="9"/><path d="M12 3v18M7 8c2 1 3 3 5 3M17 8c-2 1-3 3-5 3M7 16c2-1 3-2 5-2M17 16c-2-1-3-2-5-2"/></svg></span>
      <h3>Specialized Diagnostics</h3>
      <p>Advanced diagnostic testing and imaging services to accurately identify health conditions and develop effective treatment strategies.</p>
      <ul><li>Advanced Imaging</li><li>Laboratory Services</li><li>Health Screenings</li></ul>
      <a class="more" href="#">Learn More <svg width="10" height="10" viewBox="0 0 24 24" fill="none" stroke="#2b8cc4" stroke-width="2.5"><path d="M4 12h16M14 6l6 6-6 6"/></svg></a>
    </article>
    <article class="service-card">
      <span class="service-icon"><svg width="20" height="20" viewBox="0 0 24 24" fill="none" stroke="#fff" stroke-width="2"><path d="M12 21s-8-5-8-11a4.5 4.5 0 0 1 8-2.8A4.5 4.5 0 0 1 20 10c0 6-8 11-8 11z"/></svg></span>
      <h3>Preventive Health</h3>
      <p>Proactive health programs designed to prevent illness, promote wellness, and help you maintain optimal health throughout your life.</p>
      <ul><li>Lifestyle Counseling</li><li>Nutrition Planning</li><li>Mental Health Support</li></ul>
      <a class="more" href="#">Learn More <svg width="10" height="10" viewBox="0 0 24 24" fill="none" stroke="#2b8cc4" stroke-width="2.5"><path d="M4 12h16M14 6l6 6-6 6"/></svg></a>
    </article>
  </div>
</section>

<section class="portfolio">
  <div class="section-head">
    <span class="tag">Our Portfolio</span>
    <h2 class="serif">A Glimpse Into Our Practice</h2>
    <p>Explore our state-of-the-art facilities, meet our dedicated team, and see the compassionate care we provide every day.</p>
  </div>
  <div class="gallery">
    <div class="gallery-item" role="img" aria-label="Bright clinic waiting room with blue chairs and plants" style="background:linear-gradient(135deg,#f1f4f6,#c7d8e2 60%,#6d93ae)"></div>
    <div class="gallery-item" role="img" aria-label="Medical team standing together in a hospital corridor" style="background:linear-gradient(180deg,#c9a98a,#e8eef2 45%,#3e5d86)"></div>
    <div class="gallery-item" role="img" aria-label="Modern operating room with surgical lights and monitors" style="background:linear-gradient(135deg,#d9ecf5,#9fc6dc 60%,#6f9fbd)"></div>
    <div class="gallery-item" role="img" aria-label="Doctor holding hands with an elderly patient" style="background:linear-gradient(135deg,#d8d6d2,#c3ab93 55%,#8a6d55)"></div>
    <div class="gallery-item" role="img" aria-label="Two doctors consulting a patient at a desk" style="background:linear-gradient(135deg,#eef2f5,#c9d6de 60%,#9fb3c2)"></div>
    <div class="gallery-item" role="img" aria-label="Portrait of a smiling doctor in a white coat" style="background:linear-gradient(180deg,#7a5a42,#d3b497 40%,#eef0f2 75%,#2d4a74)"></div>
  </div>
</section>

<section class="contact">
  <div class="section-head">
    <span class="tag">Get In Touch</span>
    <h2 class="serif">We're Here to Help</h2>
    <p>Have questions or ready to schedule your appointment? Reach out to our friendly team and we'll be happy to assist you.</p>
  </div>
  <div class="contact-info">
    <h3>Contact Information</h3>
    <div class="info-grid">
      <div class="info-card"><span class="service-icon"><svg width="16" height="16" viewBox="0 0 24 24" fill="none" stroke="#fff" stroke-width="2"><path d="M12 22s7-6.5 7-12a7 7 0 0 0-14 0c0 5.5 7 12 7 12z"/><circle cx="12" cy="10" r="2.5"/></svg></span><h4>Visit Us</h4><p>48 Linden Park Road<br>Eastbrook, MD 20714</p></div>
      <div class="info-card"><span class="service-icon"><svg width="16" height="16" viewBox="0 0 24 24" fill="none" stroke="#fff" stroke-width="2"><path d="M5 3h4l2 5-2.5 1.5a11 11 0 0 0 6 6L16 13l5 2v4a2 2 0 0 1-2 2A16 16 0 0 1 3 5a2 2 0 0 1 2-2z"/></svg></span><h4>Call Us</h4><p>(555) 284-9130<br>(555) 284-9131</p></div>
      <div class="info-card"><span class="service-icon"><svg width="16" height="16" viewBox="0 0 24 24" fill="none" stroke="#fff" stroke-width="2"><rect x="3" y="5" width="18" height="14" rx="2"/><path d="M3 7l9 6 9-6"/></svg></span><h4>Email Us</h4><p>info@marbletonhealth.com<br>appointments@marbletonhealth.com</p></div>
      <div class="info-card"><span class="service-icon"><svg width="16" height="16" viewBox="0 0 24 24" fill="none" stroke="#fff" stroke-width="2"><circle cx="12" cy="12" r="9"/><path d="M12 7v5l3 2"/></svg></span><h4>Working Hours</h4><p>Mon - Fri: 8:00 AM - 6:00 PM<br>Sat: 9:00 AM - 2:00 PM</p></div>
    </div>
  </div>
  <form class="contact-form">
    <h3>Send Us a Message</h3>
    <div class="field-row">
      <div class="field"><label>Full Name *</label><div class="input">John Doe</div></div>
      <div class="field"><label>Email Address *</label><div class="input">john@example.com</div></div>
    </div>
    <div class="field"><label>Phone Number</label><div class="input">(555) 000-0000</div></div>
    <div class="field"><label>Your Message *</label><div class="input textarea">How can we help you today?</div></div>
    <div class="consent"><i></i><span>I'd like to receive health tips, updates, and exclusive offers from Marbleton Health. You can unsubscribe at any time.</span></div>
    <div class="btn btn-primary send"><svg width="12" height="12" viewBox="0 0 24 24" fill="none" stroke="#fff" stroke-width="2"><path d="M22 2L11 13M22 2l-7 20-4-9-9-4z"/></svg>Send Message</div>
    <p class="fine">By submitting this form, you agree to our privacy policy. Your information is secure and will never be shared.</p>
  </form>
</section>

<footer class="site-footer">
  <div class="footer-cols">
    <div>
      <div class="footer-brand">Marbleton Health</div>
      <p class="footer-about">Providing compassionate, patient-centered healthcare with modern facilities and experienced medical professionals.</p>
      <div class="socials"><span></span><span></span><span></span><span></span></div>
    </div>
    <div><h5>Quick Links</h5><ul class="footer-list"><li>Home</li><li>About</li><li>Services</li><li>Portfolio</li><li>Contact</li></ul></div>
    <div><h5>Our Services</h5><ul class="footer-list"><li>Primary Care</li><li>Specialized Diagnostics</li><li>Preventive Health</li><li>Chronic Disease Management</li><li>Mental Health Support</li></ul></div>
    <div><h5>Contact Us</h5>
      <div class="footer-contact">
        <p>48 Linden Park Road<br>Eastbrook, MD 20714</p>
        <p>Phone: (555) 284-9130</p>
        <p>Email: info@marbletonhealth.com</p>
        <p>Mon - Fri: 8:00 AM - 6:00 PM<br>Sat: 9:00 AM - 2:00 PM</p>
      </div>
    </div>
  </div>
  <div class="footer-bottom">
    <span>© 2026 Marbleton Health. All rights reserved.</span>
    <nav><a href="#">Privacy Policy</a><a href="#">Terms of Service</a><a href="#">Accessibility</a></nav>
  </div>
</footer>

</body>
</html>
```